Business Card

Just need business logo with phone number on it. 0472 318 506
And the following on the bottom of the card.

"Your local plumbing experts".
and emblems for kovo card, cheque and cash

```html
<!DOCTYPE html>
<html lang="en">
<head>
<meta charset="utf-8">
<title>Ridgeline Plumbing &amp; Drainage – Business Card</title>
<link href="https://fonts.googleapis.com/css2?family=Michroma&family=Roboto:wght@400&display=swap" rel="stylesheet">
<style>
  :root {
    --backdrop: #3a3a3c;
    --card: #f4f4f3;
    --brand-blue: #1a78c8;
    --brand-red: #d9251d;
    --cheque-yellow: #f3ee9a;
    --cheque-ink: #6b6b55;
    --cash-green: #5d9b78;
    --cash-ink: #e9f3ec;
  }
  html, body {
    margin: 0;
    width: 1200px;
    height: 902px;
    overflow: hidden;
    background: var(--backdrop);
  }
  .business-card {
    position: absolute;
    left: 100px;
    top: 165px;
    width: 1000px;
    height: 572px;
    background: var(--card);
    border-radius: 40px;
    font-family: "Roboto", sans-serif;
    color: var(--brand-blue);
  }
  .brand-name {
    position: absolute;
    left: 300px;
    top: 64px;
    width: 560px;
    font-family: "Michroma", sans-serif;
    color: var(--brand-red);
    text-align: center;
    line-height: 1;
  }
  .brand-name__main { display: block; font-size: 54px; letter-spacing: 2px; }
  .brand-name__sub { display: block; font-size: 20px; letter-spacing: 6px; margin-top: 14px; }
  .brand-name__suffix { display: block; font-size: 12px; letter-spacing: 3px; margin-top: 10px; text-align: right; }
  .phone-row {
    position: absolute;
    left: 110px;
    top: 250px;
    display: flex;
    align-items: center;
    gap: 30px;
  }
  .phone-icon { width: 54px; height: 54px; flex: none; }
  .phone-number {
    font-family: "Michroma", sans-serif;
    font-size: 62px;
    letter-spacing: 4px;
    color: var(--brand-blue);
    white-space: nowrap;
  }
  .accent-line {
    position: absolute;
    height: 4px;
    background: var(--brand-red);
    border-radius: 2px;
  }
  .accent-line--left { left: 90px; top: 346px; width: 150px; }
  .accent-line--right { left: 770px; top: 410px; width: 150px; }
  .tagline {
    position: absolute;
    left: 0;
    width: 1000px;
    top: 356px;
    margin: 0;
    text-align: center;
    font-size: 30px;
  }
  .payment-row {
    position: absolute;
    left: 190px;
    top: 468px;
    display: flex;
    align-items: center;
    gap: 26px;
  }
  .payment-label { font-size: 24px; }
  .pay-card {
    display: flex;
    align-items: center;
    gap: 8px;
    font-size: 24px;
    color: var(--brand-blue);
  }
  .pay-card__mark { width: 14px; height: 14px; background: var(--brand-blue); }
  .pay-icon { width: 92px; height: 44px; }
</style>
</head>
<body>
  <main class="business-card">
    <div class="brand-name">
      <span class="brand-name__main">RIDGELINE</span>
      <span class="brand-name__sub">PLUMBING &amp; DRAINAGE</span>
      <span class="brand-name__suffix">PTY LTD</span>
    </div>

    <div class="phone-row">
      <svg class="phone-icon" viewBox="0 0 56 56" aria-hidden="true">
        <circle cx="28" cy="28" r="24" fill="none" stroke="var(--brand-red)" stroke-width="5"/>
        <path d="M21 17c-2 1-4 3-3 7 2 7 7 12 14 15 4 1 6-1 7-3l-5-4-3 2c-3-1-6-4-7-7l2-3z" fill="var(--brand-red)"/>
      </svg>
      <span class="phone-number">0472 318 506</span>
    </div>

    <div class="accent-line accent-line--left"></div>
    <div class="accent-line accent-line--right"></div>

    <p class="tagline">Your local plumbing experts</p>

    <div class="payment-row">
      <span class="payment-label">Payment made from:</span>
      <span class="pay-card"><span class="pay-card__mark"></span>tarvin</span>
      <svg class="pay-icon" viewBox="0 0 92 44" role="img" aria-label="Cheque">
        <rect x="1" y="1" width="90" height="42" rx="3" fill="var(--cheque-yellow)"/>
        <text x="46" y="13" font-family="Roboto, sans-serif" font-size="8" fill="var(--cheque-ink)" text-anchor="middle">CHEQUE</text>
        <rect x="10" y="20" width="30" height="2" fill="var(--cheque-ink)"/>
        <rect x="10" y="28" width="50" height="2" fill="var(--cheque-ink)"/>
        <rect x="66" y="26" width="16" height="8" fill="none" stroke="var(--cheque-ink)" stroke-width="1.5"/>
      </svg>
      <svg class="pay-icon" viewBox="0 0 92 44" role="img" aria-label="Cash">
        <rect x="1" y="1" width="90" height="42" rx="3" fill="var(--cash-green)"/>
        <text x="46" y="29" font-family="Roboto, sans-serif" font-size="17" fill="var(--cash-ink)" text-anchor="middle">CA$H</text>
      </svg>
    </div>
  </main>
</body>
</html>
```